Post badge Design Project SEO/SEM Website

Need an updated more professional look for an SEO/SEM existing site.
see: www.harborkite-solvex.com

I have an existing logo (in eps format), but am flexible on color and would consider updating the logo if the current colors or design limits your creativity.

Target Market(s)

My customers tend to be marketing managers for mid-size companies with 50+ employees.

Industry/Entity Type

Marketing

Requirements
Must have
• Design should support Post badge 3.0 menus, and widgets.
Nice to have
• Should you want/need it, the font used in the logo is 'ARTLOOKIN'
Should not have
• flash

```html
<!DOCTYPE html>
<html lang="en">
<head>
<meta charset="utf-8">
<title>Harborkite Solvex</title>
<link rel="stylesheet" href="https://fonts.googleapis.com/css2?family=PT+Sans:ital,wght@0,400;0,700;1,400;1,700&display=swap">
<style>
:root{
  --page-top:#121212;
  --page-mid:#3a3a3a;
  --page-bottom:#4b4b4b;
  --shell:#2d2d2d;
  --shell-edge:#5a5a5a;
  --panel:#262626;
  --text:#b9b9b9;
  --bright:#e6e6e6;
  --cyan:#17b9ea;
  --cyan-light:#5fdcf2;
  --rule:#8a8a8a;
}
*{box-sizing:border-box;margin:0;padding:0}
html,body{width:951px;height:1200px;overflow:hidden}
body{
  position:relative;
  font-family:"PT Sans",sans-serif;
  font-weight:700;
  color:var(--text);
  background:linear-gradient(to bottom,var(--page-top) 0,var(--page-mid) 150px,var(--page-bottom) 320px,var(--page-bottom) 100%);
}
a{color:var(--cyan);text-decoration:none}
.top-rule{position:absolute;left:0;top:1px;width:951px;height:1px;background:#cfcfcf}
.main-nav{position:absolute;left:114px;top:5px;display:flex;font-size:11px}
.main-nav a{display:block;height:21px;line-height:21px;color:var(--bright)}
.main-nav .current{width:73px;text-align:center;background:linear-gradient(#27c3e9,#129fc9);border-radius:3px;color:#fff;font-weight:400}
.main-nav .item{margin-left:30px}
.main-nav .item + .item{margin-left:52px}

.brand{position:absolute;left:335px;top:58px;display:flex;align-items:center;gap:18px}
.brand-mark{width:40px;height:40px;border-radius:50%;background:#d8d8d8}
.brand-name{font-size:25px;font-variant:small-caps;color:#d9d9d9;line-height:1}
.brand-tag{font-size:9.5px;font-variant:small-caps;color:#d9d9d9;margin-top:3px;letter-spacing:.2px}

.shell{position:absolute;left:103px;top:126px;width:764px;height:966px;background:var(--shell);border:1px solid var(--shell-edge);border-radius:12px;box-shadow:0 0 6px rgba(0,0,0,.6)}

.sidebar{position:absolute;left:117px;top:140px;width:181px}
.widget-title{height:21px;background:var(--cyan);color:#10323f;font-size:12.5px;font-variant:small-caps;text-align:center;line-height:21px;position:relative}
.widget-title::before{content:"";position:absolute;left:6px;top:4px;width:13px;height:13px;background:#e3e3e3;border:1px solid #333}
.widget-title::after{content:"";position:absolute;left:10px;top:8px;border-left:6px solid #333;border-top:3px solid transparent;border-bottom:3px solid transparent}
.search-box{margin:3px 2px 8px;height:19px;background:#fff;border:1px solid #999;position:relative}
.search-box svg{position:absolute;right:4px;top:3px}
.categories{background:#222;padding:3px 5px 6px;font-size:10.5px;line-height:13px}
.categories p{margin-bottom:3px}
.cat-list{list-style:none}
.cat-list li{padding-left:14px;position:relative;line-height:16px}
.cat-list li::before{content:"";position:absolute;left:3px;top:5px;border-left:5px solid var(--cyan);border-top:3px solid transparent;border-bottom:3px solid transparent}
.cat-list .visited{color:var(--bright)}
.cat-list .hovered{color:var(--cyan-light);text-decoration:underline}

.post{position:absolute;left:308px;width:545px;background:var(--panel);border-radius:8px;padding:12px 16px 0;text-align:center;font-size:10.5px;line-height:12.4px}
.post-one{top:140px;height:273px}
.post-two{top:420px;height:615px}
.post-title{font-size:20px;font-variant:small-caps;line-height:24px;color:var(--bright)}
.post-two .post-title{color:var(--cyan)}
.post-title .hovered,.hovered{color:var(--cyan-light);text-decoration:underline}
.visited{color:var(--bright)}
.post-meta{font-size:8.5px;font-weight:400;color:var(--bright);line-height:12px}
.post-meta em{font-style:italic}
.post-body{text-align:justify;margin-top:10px}
.post-one .post-body{line-height:13.2px}
.post-body p{margin-bottom:11px}
.post-badge{float:left;width:38px;height:42px;margin:0 8px 0 5px;border-radius:50%;background:#2b6fa2;border:3px solid #d8d8d8}
sup,sub{font-size:7px;font-weight:400}
.post-footer{position:absolute;left:0;right:0;bottom:9px;font-size:8.5px;color:var(--bright)}
.post-footer em{font-weight:400}

.h{font-variant:small-caps;line-height:1}
.h1{font-size:22px;color:var(--cyan);margin-top:12px}
.h2{font-size:18px;color:var(--cyan);margin-top:10px}
.h3{font-size:14px;color:var(--bright);margin-top:12px}
.h4{font-size:12px;color:var(--bright);margin-top:11px}
.h5{font-size:11px;color:var(--bright);margin-top:12px}
.h6{font-size:10px;color:var(--cyan);margin-top:10px}
.post-two .post-body{margin-top:13px;line-height:13px}
abbr{text-decoration:none;border-bottom:1px dotted #aaa}
.sample-button{display:inline-block;width:98px;height:18px;border-radius:9px;background:var(--cyan-light);color:#0e2a33;font-size:9px;line-height:18px;text-align:center;margin:4px 0 0}
.block-heading{font-size:13px;font-variant:small-caps;color:var(--bright);text-align:center;margin-top:13px}
.list{list-style:none;margin:12px 0 0 10px;text-align:left}
.list li{padding-left:12px;position:relative;line-height:16px}
.list li::before{content:"";position:absolute;left:0;top:5px;border-left:5px solid var(--cyan);border-top:3px solid transparent;border-bottom:3px solid transparent}
.quote{margin:10px 6px 0 38px;border:1px solid var(--rule);background:#2f2f2f;font-style:italic;font-size:10px;line-height:12px;padding:3px 0 3px 24px;text-align:left;position:relative}
.quote::before{content:"\201C";position:absolute;left:2px;top:-2px;font-size:28px;line-height:28px;color:#888;font-style:normal}
.data-table{border-collapse:collapse;margin-top:10px;font-size:10px;text-align:left}
.data-table th,.data-table td{border:2px solid #8c8c8c;height:17px;width:43px;padding:0 3px}
.data-table th{height:25px;text-align:center;background:#303030}

.site-footer{position:absolute;left:117px;top:1055px;width:736px;font-size:8.5px;color:var(--bright);text-align:center}
.site-footer svg{position:absolute;left:0;top:0}
.site-footer p{line-height:14px}
</style>
</head>
<body>
<div class="top-rule"></div>
<nav class="main-nav">
  <a class="current" href="#">Home</a>
  <a class="item" href="#">Menu Item</a>
  <a class="item" href="#">About</a>
</nav>

<header class="brand">
  <div class="brand-mark"></div>
  <div>
    <div class="brand-name">Harborkite Solvex</div>
    <div class="brand-tag">Internet Marketing, Lakemere Valley 40021</div>
  </div>
</header>

<div class="shell"></div>

<aside class="sidebar">
  <div class="widget-title">Search</div>
  <div class="search-box">
    <svg width="11" height="11" viewBox="0 0 11 11"><circle cx="4.5" cy="4.5" r="3.3" fill="none" stroke="#aaa" stroke-width="1.4"/><line x1="7" y1="7" x2="10" y2="10" stroke="#aaa" stroke-width="1.6"/></svg>
  </div>
  <div class="widget-title">Categories</div>
  <div class="categories">
    <p>Lorem ipsum dolor sit amet. Nam sit amet sem. Mauris a ante.</p>
    <ul class="cat-list">
      <li><a href="#">All News</a> (50)</li>
      <li><a href="#">Best of the Year</a> (4)</li>
      <li><a href="#">Hyperlink</a> (24)</li>
      <li><a class="visited" href="#">Visited link</a> (17)</li>
      <li><a class="hovered" href="#">Hovered link</a> (6)</li>
    </ul>
  </div>
</aside>

<article class="post post-one">
  <h2 class="post-title">Text, <a href="#">Link</a>, <span class="visited">Visited</span>, <a class="hovered" href="#">Hovered</a></h2>
  <div class="post-meta">Published November 05, 2008 | By <em>admin</em> | <em>Edit</em></div>
  <div class="post-body">
    <p><span class="post-badge" role="img" aria-label="Post badge image"></span>Lorem <sup>superscript</sup> dolor <sub>subscript</sub> amet, consectetuer adipiscing <a href="#">link</a>, <span class="visited">visited link</span>, <a class="hovered" href="#">hovered link</a> consectetuer adipiscing elit. Quisque sed felis. Aliquam sit amet felis. Mauris semper, velit semper laoreet dictum, quam diam dictum urna, nec placerat elit nisl <span class="visited">one more link</span> in quam. Etiam augue pede, molestie eget, rhoncus at, convallis ut, eros.</p>
    <p>Aliquam pharetra. Nulla in tellus eget odio sagittis blandit.Maecenas at nisl. Nullam lorem mi, eleifend a, fringilla vel, semper at, ligula. Mauris eu wisi. Ut ante dui, aliquet nec, congue non, accumsan sit amet, lectus. Mauris et mauris. Duis sed massa id mauris pretium venenatis. Suspendisse cursus velit vel ligula. Mauris elit.</p>
    <p>Aliquam pharetra. Nulla in tellus eget odio sagittis blandit.Maecenas at nisl. Nullam lorem mi, eleifend a, fringilla vel, semper at, ligula. Mauris eu wisi. Ut ante dui, aliquet nec, congue non, accumsan sit amet, lectus. Mauris et mauris. Duis sed massa id mauris pretium venenatis. Suspendisse cursus velit vel ligula. Mauris elit.</p>
  </div>
  <div class="post-footer">Category: No Category | Tags: <em>link</em>, <em>visited</em>, <em class="hovered">hovered</em> | <em>No Comments »</em></div>
</article>

<article class="post post-two">
  <h2 class="post-title">Worth A Thousand Words</h2>
  <div class="post-meta">Published September 11, 2008 | By <em>admin</em> | <em>Edit</em></div>
  <div class="h h1">Heading 1</div>
  <div class="h h2">Heading 2</div>
  <div class="h h3">Heading 3</div>
  <div class="h h4">Heading 4</div>
  <div class="h h5">Heading 5</div>
  <div class="h h6">Heading 6</div>
  <div class="post-body">
    <p>Lorem <sup>superscript</sup> dolor <sub>subscript</sub> amet, consectetuer adipiscing elit, <span class="visited">test link</span>. Nullam dignissim convallis est. Quisque aliquam. <em>cite</em>. Nunc iaculis suscipit dui. Nam sit amet sem. Aliquam libero nisi, imperdiet at, tincidunt nec, gravida vehicula, nisl. Praesent mattis, massa quis luctus fermentum, turpis mi volutpat justo, eu volutpat enim diam eget metus. Maecenas ornare tortor. Donec sed tellus eget sapien fringilla nonummy. <abbr>QRX</abbr> Mauris a ante. Suspendisse quam sem, consequat at, commodo vitae, feugiat in, nunc. Morbi imperdiet augue quis tellus.<abbr>AVE</abbr></p>
    <span class="sample-button">Sample Button</span>
    <div class="block-heading">List</div>
    <ul class="list">
      <li>List Item 1</li>
      <li>List Item 2</li>
      <li>List Item 3</li>
    </ul>
    <div class="block-heading">Quote</div>
    <blockquote class="quote">"Lorem ipsum dolor sit amet, consectetur adipiscing elit."<br>–Blockquote</blockquote>
    <div class="block-heading">Table</div>
    <table class="data-table">
      <tr><th>Header</th><th>Header</th><th>Header</th></tr>
      <tr><td>Data</td><td>Data</td><td>Data</td></tr>
      <tr><td>Data</td><td>Data</td><td>Data</td></tr>
      <tr><td>Data</td><td>Data</td><td>Data</td></tr>
    </table>
  </div>
  <div class="post-footer">Category: No Category | Tags: <em>link</em>, <em>visited</em>, <em class="hovered">hovered</em> | <em>No Comments »</em></div>
</article>

<footer class="site-footer">
  <svg width="16" height="16" viewBox="0 0 16 16"><rect width="16" height="16" rx="3" fill="#f28a1d"/><circle cx="4.5" cy="11.5" r="1.6" fill="#fff"/><path d="M3 7.5a5.5 5.5 0 0 1 5.5 5.5" stroke="#fff" stroke-width="1.7" fill="none"/><path d="M3 3.5a9.5 9.5 0 0 1 9.5 9.5" stroke="#fff" stroke-width="1.7" fill="none"/></svg>
  <p>Copyright © 2007-2012 Harborkite Solvex, LLC</p>
</footer>
</body>
</html>
```